Tiltwave Drinks, Packaging Design Project

We need an awesome package design for Tiltwave Drinks' initial product launch.

Our company was founded with the idea of creating an innovative alcoholic beverage product that caters to a previously under-served market of millenials aged 21-30 who love to have a good time. The product will be served in a box with a plastic bladder and a spigot.

**Although our product will be served in a box similar to Cordelle or Hanna Strom, we are NOT in the wine category. TiltWave will focus on spirit based beverages.

We've chosen a great logo to use as the foundation for our package design. We will attach a jpeg version for your reference. You do NOT need to stick to the colors that we have used for the logo - but your colors should be bold, fun, and inviting.

We're looking forward to seeing your work!

-K7
Updates

Hey All!

Thanks so much for your contributions so far!! We want to clarify a couple things as we move forward.  Our product will be a spirit-based alcoholic beverage in a box.  We Tiltwave is more reminiscent of "portable jungle juice" rather than repackaged table wine.  We'll be looking at designs that aim younger and and are a little more daring.  We hope this helps to clarify our goals.

We're also looking at differentiating through alternative package dimensions.  Though we want to stay with a 5 liter size, we would be interested in looking at dimensions that look more like a boombox (longer and shorter than a Cordelle box).   

One possible combination would be 30 cm wide x 18 cm high x 11 cm deep.  Though you do not to adhere to these dimensions, we hope it will help by providing you with further direction.

Thanks SO much and we're looking forward to working with you!

 - K7

Industry/Entity Type

Plastic

```html
<!DOCTYPE html>
<html lang="en">
<head>
<meta charset="utf-8">
<title>Tiltwave Drinks – 5 Litre Box Front</title>
<link rel="stylesheet" href="https://fonts.googleapis.com/css2?family=Jost:wght@400;500&display=swap">
<style>
  :root {
    --page: #ffffff;
    --panel-edge: #2b2b2b;
    --brand-orange: #ee5a24;
    --wine: #7a1836;
    --splash-light: #d9718f;
    --splash-mid: #b3194f;
    --splash-dark: #3a0a1b;
    --label-white: #ffffff;
  }
  html, body {
    margin: 0;
    padding: 0;
    width: 1176px;
    height: 1200px;
    overflow: hidden;
    background: var(--page);
  }
  .canvas {
    position: relative;
    width: 1176px;
    height: 1200px;
    font-family: "Jost", "Futura", sans-serif;
  }
  .box-front {
    position: absolute;
    left: 123px;
    top: 101px;
    width: 920px;
    height: 980px;
    border: 1px solid var(--panel-edge);
    background: var(--page);
    box-shadow: 4px 4px 5px rgba(0, 0, 0, 0.45);
    overflow: hidden;
  }
  .pour-splash {
    position: absolute;
    left: 0;
    top: 0;
    width: 920px;
    height: 980px;
  }
  .brand {
    position: absolute;
    right: 50px;
    top: 78px;
    text-align: right;
    color: var(--brand-orange);
    font-weight: 500;
    line-height: 1;
  }
  .brand-name {
    display: block;
    font-size: 108px;
    letter-spacing: 1px;
  }
  .brand-descriptor {
    display: block;
    margin-top: 10px;
    font-size: 30px;
    letter-spacing: 9px;
    margin-right: -9px;
  }
  .flavour-lines {
    position: absolute;
    right: 48px;
    top: 268px;
    margin: 0;
    text-align: right;
    color: var(--wine);
    font-weight: 400;
    font-size: 22px;
    letter-spacing: 1.5px;
    line-height: 33px;
  }
  .volume {
    position: absolute;
    right: 44px;
    bottom: 28px;
    color: var(--label-white);
    font-weight: 400;
    line-height: 1;
  }
  .volume-number { font-size: 46px; }
  .volume-unit { font-size: 30px; }
</style>
</head>
<body>
<div class="canvas">
  <section class="box-front">
    <svg class="pour-splash" role="img" aria-label="Photograph of red drink pouring in a diagonal stream and splashing" viewBox="0 0 920 980">
      <defs>
        <linearGradient id="splashTone" x1="0" y1="0" x2="1" y2="1">
          <stop offset="0" stop-color="var(--splash-mid)"/>
          <stop offset="0.55" stop-color="var(--splash-dark)"/>
          <stop offset="0.8" stop-color="var(--splash-light)"/>
          <stop offset="1" stop-color="var(--splash-dark)"/>
        </linearGradient>
      </defs>
      <polygon points="0,30 250,110 520,300 920,720 920,980 0,980" fill="url(#splashTone)"/>
    </svg>

    <h1 class="brand" aria-label="Tiltwave Drinks">
      <span class="brand-name">TILTWAVE</span>
      <span class="brand-descriptor">DRINKS</span>
    </h1>

    <p class="flavour-lines">
      OMOMOMOMOMO<br>
      MOMOMOMOMOM<br>
      MOMOMOMOMOM
    </p>

    <p class="volume"><span class="volume-number">5</span><span class="volume-unit">Litres</span></p>
  </section>
</div>
</body>
</html>
```